OLUM Sign
OLUM leasing sign
#12 I'd like to go with this design with a few minor changes. Could you please change the font of Daniel Pruett to something that works better with the other font Office space? and can you remove the rectangles under the phone number? I promise i'll respond more quickly once i see the revisions.
additional comment on 23 -24. I think I like these for their clean simplicity (although they need the required information and the proper logo)
#23 ,#24 These looks different - good. Can you try a grey background, with correct logo (maybe in white). There is now an .eps file available. The sign must have phone number, "Office Space", and Realtor's name. use only the colors in logo, and black.
Dear PH, thanks for your valuable feedback.Will submit some more design options...regards,
will upload vector file. these designs are not what we are looking for. we want an eye catching creative design that doesn't look like a typical leasing sign.
Dear PH, Can you please upload the vector file (.ai or .eps) of the logo.Regards.

```html
<!DOCTYPE html>
<html lang="en">
<head>
<meta charset="utf-8">
<title>OLUM Leasing Sign</title>
<link rel="stylesheet" href="https://fonts.googleapis.com/css2?family=Archivo+Black&family=Russo+One&family=Nunito:wght@900&family=Libre+Baskerville&display=swap">
<style>
  :root {
    --sign-red: #c8101a;
    --banner-edge: #7a0a0e;
    --ink: #141414;
    --outline-dark: #2a0d0d;
    --gold-edge: #e8c35a;
    --cream-top: #ffffff;
    --cream-bottom: #fbe7a6;
    --logo-grey: #8a8a8a;
    --frame-grey: #9b9b9b;
    --white: #ffffff;
  }
  * { margin: 0; padding: 0; box-sizing: border-box; }
  html, body { width: 1200px; height: 799px; overflow: hidden; background: #ffffff; }
  .sign {
    position: relative;
    width: 1200px;
    height: 799px;
    background: linear-gradient(180deg, var(--cream-top) 22%, var(--cream-bottom) 100%);
    overflow: hidden;
  }
  .banner {
    position: absolute;
    left: 0; top: 0;
    width: 1200px; height: 205px;
    background: var(--sign-red);
    border-bottom: 4px solid var(--banner-edge);
    display: flex; align-items: center; justify-content: center;
  }
  .banner-title {
    font-family: "Archivo Black", sans-serif;
    font-size: 134px;
    line-height: 1;
    color: var(--white);
    letter-spacing: 2px;
    -webkit-text-stroke: 3px var(--outline-dark);
    paint-order: stroke fill;
    text-shadow: 3px 3px 0 var(--outline-dark);
  }
  .space-type {
    position: absolute;
    left: 0; top: 238px;
    width: 1200px;
    text-align: center;
    font-family: "Russo One", sans-serif;
    font-size: 112px;
    line-height: 1;
    letter-spacing: 6px;
    color: var(--sign-red);
    -webkit-text-stroke: 4px var(--outline-dark);
    paint-order: stroke fill;
  }
  .phone-line {
    position: absolute;
    left: 46px; top: 374px;
    display: flex; align-items: center; gap: 28px;
  }
  .phone-icon { width: 66px; height: 92px; }
  .phone-number {
    font-family: "Nunito", sans-serif;
    font-weight: 900;
    font-size: 136px;
    line-height: 1;
    letter-spacing: 4px;
    color: var(--ink);
    -webkit-text-stroke: 8px var(--gold-edge);
    paint-order: stroke fill;
  }
  .contact-label {
    position: absolute;
    right: 30px; top: 535px;
    font-family: "Libre Baskerville", serif;
    font-size: 48px;
    line-height: 1;
    color: var(--ink);
  }
  .contact-rule {
    position: absolute;
    left: 600px; top: 596px;
    width: 576px; height: 3px;
    background: var(--ink);
  }
  .agent-name {
    position: absolute;
    right: 30px; top: 614px;
    font-family: "Russo One", sans-serif;
    font-size: 54px;
    line-height: 1;
    letter-spacing: 3px;
    text-transform: uppercase;
    color: var(--sign-red);
    -webkit-text-stroke: 2px var(--outline-dark);
    paint-order: stroke fill;
  }
  .brand-panel {
    position: absolute;
    left: 19px; top: 605px;
    width: 557px; height: 210px;
    background: var(--white);
    border: 4px solid var(--frame-grey);
    display: flex; align-items: center; justify-content: center; gap: 26px;
    padding-bottom: 16px;
  }
  .brand-mark {
    width: 40px; height: 40px;
    background: var(--sign-red);
  }
  .brand-name {
    font-family: "Archivo Black", sans-serif;
    font-size: 110px;
    line-height: 1;
    color: var(--logo-grey);
    letter-spacing: 4px;
  }
</style>
</head>
<body>
  <main class="sign">
    <header class="banner">
      <h1 class="banner-title">AVAILABLE</h1>
    </header>

    <h2 class="space-type">OFFICE SPACE</h2>

    <div class="phone-line">
      <svg class="phone-icon" viewBox="0 0 24 30" aria-hidden="true">
        <path fill="#141414" d="M7.5 1.5c-1.2-.8-2.6-.4-3.3.7L2.6 4.8C1 7.4.7 12 2.3 17.2c1.7 5.4 5 9.4 7.9 11 1.2.6 2.600.3 3.4-.7l1.8-2.3c.8-1 .5-2.4-.5-3.1l-2.3-1.6c-.9-.6-2.1-.5-2.8.3l-.9 1c-1.7-1.5-3.3-4.4-3.9-7.2l1.2-.5c1-.4 1.5-1.5 1.2-2.6l-.8-2.7c-.3-1.1-.9-2-1.7-2.5z"/>
      </svg>
      <span class="phone-number">215-555-0148</span>
    </div>

    <p class="contact-label">Contact Person</p>
    <div class="contact-rule"></div>
    <p class="agent-name">Daniel Pruett</p>

    <div class="brand-panel">
      <span class="brand-mark"></span>
      <span class="brand-name">OLUM</span>
    </div>
  </main>
</body>
</html>
```